Investment Management Model Portfolio PDF Flyer

Our clients are retirees and soon-to-be retirees looking for help managing their investment portfolio. Our company designed model portfolios that offer more customization options than competitors' model portfolios. We want to show potential clients that we can provide customization (i.e. "tilts") that allow personalization. Clients can opt for portfolios with more dividends, international exposure, socially-responsible ESG choices, and anything inbetween. Unlike competitors our approach is not one-size-fits-all.

The process of building a portfolio lends itself to metaphors or pictures to do with: building a custom portfolio (DIY-friendly), global diversification (accessing global markets instead of just local markets), and environmentally & socially responsible options (clean energy, rain forest)

Target Market(s)

Seniors (age 65+), retired persons, investors

Industry/Entity Type

Financial Planning

Font styles to use
Serif
Other font styles liked:
• Rufina Bold, Rufina

Colors
ec1f27
0356a4

Requirements
Must have
• -Must use color palette in attached PDF
-Must use pie chart / doughnut chart to represent asset allocation
-At least 4 "asset allocations" for basic benchmark (20/80, 40/60, 60/40, 80/20)
-At least 3 "tilts" are described as Dividend, ESG, and International
Nice to have
• -Asset allocations can be named: conservative, conservative growth, moderate, and growth (20/80, 40/60, 60/40, 80/20, respectively)
-Dividend paying, international and ESG could be represented in pictures or graphics (dividends = money returned to client, international could show a globe or try to represent global markets/currency, ESG is often connected to environmental causes but not only)
Should not have
• -Projected rates of returns

```html
<!DOCTYPE html>
<html lang="en">
<head>
<meta charset="utf-8">
<title>Personalize Your Blueprint+ | Heron Retirement Planning</title>
<link rel="stylesheet" href="https://fonts.googleapis.com/css2?family=Rufina:wght@400;700&display=swap">
<style>
  :root {
    --blue: #1558a4;
    --red: #ec1f27;
    --green: #63ad2a;
    --purple: #a8178e;
    --ink: #0d0d0d;
    --paper: #ffffff;
    --frame: #cccccc;
  }
  * { box-sizing: border-box; margin: 0; padding: 0; }
  html, body { width: 943px; height: 1200px; overflow: hidden; }
  body {
    position: relative;
    background: var(--frame);
    font-family: "Rufina", Georgia, serif;
    color: var(--ink);
  }
  .sheet {
    position: absolute; left: 31px; top: 33px;
    width: 879px; height: 1137px;
    background: var(--paper);
  }
  .abs { position: absolute; }

  /* Header */
  .brand-mark { left: 105px; top: 101px; width: 46px; height: 46px; background: var(--red); }
  .brand-name { left: 164px; top: 94px; font-size: 46px; line-height: 1; letter-spacing: 1px; color: var(--ink); }
  .brand-sub { left: 166px; top: 142px; font-size: 14.5px; letter-spacing: 1.6px; text-transform: uppercase; color: var(--ink); }
  .contact { right: 108px; top: 106px; text-align: right; font-size: 17px; line-height: 24px; }

  .page-title {
    left: 103px; top: 186px; width: 734px;
    font-size: 55px; font-weight: 700; line-height: 1; white-space: nowrap;
    letter-spacing: -0.4px;
  }
  .rule { left: 103px; width: 734px; height: 3px; background: var(--ink); }
  .rule-top { top: 248px; }
  .rule-bottom { top: 1104px; height: 2.5px; }

  .section-title { font-size: 35px; font-weight: 700; line-height: 1; white-space: nowrap; letter-spacing: -0.3px; }
  .section-split { left: 104px; top: 279px; }
  .section-tilt { right: 106px; top: 703px; }

  /* Split legends */
  .split-key { width: 150px; text-align: center; }
  .split-key .ratio { font-size: 22px; line-height: 1; letter-spacing: 0.5px; }
  .split-key .swatches { display: flex; justify-content: space-between; margin: 9px 0 0; }
  .split-key .item { width: 62px; display: flex; flex-direction: column; align-items: center; font-size: 20px; line-height: 1; }
  .split-key .item i { display: block; width: 24px; height: 24px; margin-bottom: 8px; }

  .blue { background: var(--blue); }
  .red { background: var(--red); }
  .green { background: var(--green); }
  .purple { background: var(--purple); }

  /* Tilt legends */
  .tilt-title { font-size: 24px; font-weight: 700; line-height: 1; white-space: nowrap; }
  .tilt-list { list-style: none; }
  .tilt-list li { display: flex; align-items: center; height: 26px; font-size: 15px; }
  .tilt-list li i { display: block; width: 23px; height: 23px; margin-right: 14px; flex: none; }

  /* Donuts */
  .donut { width: 160px; height: 160px; }
  .donut text { font-family: "Rufina", Georgia, serif; font-size: 12px; font-weight: 700; fill: #fff; text-anchor: middle; dominant-baseline: middle; }
  .donut .seg { fill: none; stroke-width: 35.5; }
  .donut .gap { stroke: #fff; stroke-width: 1.4; }
</style>
</head>
<body>
<div class="sheet"></div>

<header>
  <div class="abs brand-mark"></div>
  <div class="abs brand-name">HERON</div>
  <div class="abs brand-sub">Retirement Planning, Inc.</div>
  <div class="abs contact">www.planwithheron.com<br>Call Us: 555-014-2290</div>
</header>

<h1 class="abs page-title">Personalize Your Blueprint+</h1>
<div class="abs rule rule-top"></div>

<h2 class="abs section-title section-split">1. START WITH STOCK/BOND SPLIT</h2>

<!-- 20/80 -->
<svg class="abs donut" style="left:99px;top:338px" viewBox="0 0 160 160" aria-label="20% stocks, 80% bonds">
  <g transform="rotate(-90 80 80)">
    <circle class="seg" cx="80" cy="80" r="54" pathLength="100" stroke="var(--blue)" stroke-dasharray="20 80"/>
    <circle class="seg" cx="80" cy="80" r="54" pathLength="100" stroke="var(--red)" stroke-dasharray="80 20" stroke-dashoffset="-20"/>
  </g>
  <line class="gap" x1="80" y1="7" x2="80" y2="45"/>
  <line class="gap" x1="80" y1="7" x2="80" y2="45" transform="rotate(72 80 80)"/>
  <text x="112" y="37">20%</text><text x="48" y="124">80%</text>
</svg>
<div class="abs split-key" style="left:298px;top:412px">
  <div class="ratio">20/80</div>
  <div class="swatches"><span class="item"><i class="blue"></i>Stocks</span><span class="item"><i class="red"></i>Bonds</span></div>
</div>

<!-- 60/40 -->
<svg class="abs donut" style="left:488px;top:338px" viewBox="0 0 160 160" aria-label="60% stocks, 40% bonds">
  <g transform="rotate(-90 80 80)">
    <circle class="seg" cx="80" cy="80" r="54" pathLength="100" stroke="var(--blue)" stroke-dasharray="60 40"/>
    <circle class="seg" cx="80" cy="80" r="54" pathLength="100" stroke="var(--red)" stroke-dasharray="40 60" stroke-dashoffset="-60"/>
  </g>
  <line class="gap" x1="80" y1="7" x2="80" y2="45"/>
  <line class="gap" x1="80" y1="7" x2="80" y2="45" transform="rotate(216 80 80)"/>
  <text x="131" y="97">60%</text><text x="29" y="63">40%</text>
</svg>
<div class="abs split-key" style="left:687px;top:345px">
  <div class="ratio">80/20</div>
  <div class="swatches"><span class="item"><i class="blue"></i>Stocks</span><span class="item"><i class="red"></i>Bonds</span></div>
</div>

<!-- 40/60 -->
<div class="abs split-key" style="left:104px;top:596px">
  <div class="ratio">40/60</div>
  <div class="swatches"><span class="item"><i class="blue"></i>Stocks</span><span class="item"><i class="red"></i>Bonds</span></div>
</div>
<svg class="abs donut" style="left:295px;top:522px" viewBox="0 0 160 160" aria-label="40% stocks, 60% bonds">
  <g transform="rotate(-90 80 80)">
    <circle class="seg" cx="80" cy="80" r="54" pathLength="100" stroke="var(--blue)" stroke-dasharray="40 60"/>
    <circle class="seg" cx="80" cy="80" r="54" pathLength="100" stroke="var(--red)" stroke-dasharray="60 40" stroke-dashoffset="-40"/>
  </g>
  <line class="gap" x1="80" y1="7" x2="80" y2="45"/>
  <line class="gap" x1="80" y1="7" x2="80" y2="45" transform="rotate(144 80 80)"/>
  <text x="131" y="63">40%</text><text x="29" y="97">60%</text>
</svg>
<div class="abs split-key" style="left:489px;top:533px">
  <div class="ratio">60/40</div>
  <div class="swatches"><span class="item"><i class="blue"></i>Stocks</span><span class="item"><i class="red"></i>Bonds</span></div>
</div>

<!-- 80/20 -->
<svg class="abs donut" style="left:685px;top:522px" viewBox="0 0 160 160" aria-label="80% stocks, 20% bonds">
  <g transform="rotate(-90 80 80)">
    <circle class="seg" cx="80" cy="80" r="54" pathLength="100" stroke="var(--blue)" stroke-dasharray="80 20"/>
    <circle class="seg" cx="80" cy="80" r="54" pathLength="100" stroke="var(--red)" stroke-dasharray="20 80" stroke-dashoffset="-80"/>
  </g>
  <line class="gap" x1="80" y1="7" x2="80" y2="45"/>
  <line class="gap" x1="80" y1="7" x2="80" y2="45" transform="rotate(288 80 80)"/>
  <text x="112" y="124">80%</text><text x="48" y="37">20%</text>
</svg>

<h2 class="abs section-title section-tilt">2. TILT YOUR PREFERENCES</h2>

<!-- International -->
<svg class="abs donut" style="left:98px;top:761px" viewBox="0 0 160 160" aria-label="International tilt allocation">
  <g transform="rotate(-90 80 80)">
    <circle class="seg" cx="80" cy="80" r="54" pathLength="100" stroke="var(--blue)" stroke-dasharray="56 44"/>
    <circle class="seg" cx="80" cy="80" r="54" pathLength="100" stroke="var(--red)" stroke-dasharray="32 68" stroke-dashoffset="-56"/>
    <circle class="seg" cx="80" cy="80" r="54" pathLength="100" stroke="var(--green)" stroke-dasharray="6 94" stroke-dashoffset="-88"/>
    <circle class="seg" cx="80" cy="80" r="54" pathLength="100" stroke="var(--purple)" stroke-dasharray="6 94" stroke-dashoffset="-94"/>
  </g>
  <line class="gap" x1="80" y1="7" x2="80" y2="45"/>
  <line class="gap" x1="80" y1="7" x2="80" y2="45" transform="rotate(201.6 80 80)"/>
  <line class="gap" x1="80" y1="7" x2="80" y2="45" transform="rotate(316.8 80 80)"/>
  <line class="gap" x1="80" y1="7" x2="80" y2="45" transform="rotate(338.4 80 80)"/>
  <text x="133" y="90">56%</text><text x="27" y="90">32%</text><text x="51" y="35">6%</text><text x="70" y="27">6%</text>
</svg>
<div class="abs tilt-title" style="left:106px;top:933px">International</div>
<ul class="abs tilt-list" style="left:105px;top:974px">
  <li><i class="blue"></i>International Stocks</li>
  <li><i class="red"></i>Domestic Stocks</li>
  <li><i class="green"></i>Government Bonds</li>
  <li><i class="purple"></i>Corporate Bonds</li>
</ul>

<!-- Socially-Responsible -->
<div class="abs tilt-title" style="left:357px;top:767px">Socially-Responsible</div>
<ul class="abs tilt-list" style="left:382px;top:805px">
  <li><i class="blue"></i>ESG</li>
  <li><i class="red"></i>Stocks</li>
  <li><i class="green"></i>Government Bonds</li>
  <li><i class="purple"></i>Corporate Bonds</li>
</ul>
<svg class="abs donut" style="left:389px;top:925px" viewBox="0 0 160 160" aria-label="Socially-responsible tilt allocation">
  <g transform="rotate(-90 80 80)">
    <circle class="seg" cx="80" cy="80" r="54" pathLength="100" stroke="var(--blue)" stroke-dasharray="50 50"/>
    <circle class="seg" cx="80" cy="80" r="54" pathLength="100" stroke="var(--red)" stroke-dasharray="20 80" stroke-dashoffset="-50"/>
    <circle class="seg" cx="80" cy="80" r="54" pathLength="100" stroke="var(--green)" stroke-dasharray="15 85" stroke-dashoffset="-70"/>
    <circle class="seg" cx="80" cy="80" r="54" pathLength="100" stroke="var(--purple)" stroke-dasharray="15 85" stroke-dashoffset="-85"/>
  </g>
  <line class="gap" x1="80" y1="7" x2="80" y2="45"/>
  <line class="gap" x1="80" y1="7" x2="80" y2="45" transform="rotate(180 80 80)"/>
  <line class="gap" x1="80" y1="7" x2="80" y2="45" transform="rotate(252 80 80)"/>
  <line class="gap" x1="80" y1="7" x2="80" y2="45" transform="rotate(306 80 80)"/>
  <text x="134" y="80">50%</text><text x="48" y="124">20%</text><text x="27" y="72">15%</text><text x="56" y="32">15%</text>
</svg>

<!-- Dividend -->
<svg class="abs donut" style="left:685px;top:761px" viewBox="0 0 160 160" aria-label="Dividend tilt allocation">
  <g transform="rotate(-90 80 80)">
    <circle class="seg" cx="80" cy="80" r="54" pathLength="100" stroke="var(--blue)" stroke-dasharray="65 35"/>
    <circle class="seg" cx="80" cy="80" r="54" pathLength="100" stroke="var(--red)" stroke-dasharray="25 75" stroke-dashoffset="-65"/>
    <circle class="seg" cx="80" cy="80" r="54" pathLength="100" stroke="var(--green)" stroke-dasharray="5 95" stroke-dashoffset="-90"/>
    <circle class="seg" cx="80" cy="80" r="54" pathLength="100" stroke="var(--purple)" stroke-dasharray="5 95" stroke-dashoffset="-95"/>
  </g>
  <line class="gap" x1="80" y1="7" x2="80" y2="45"/>
  <line class="gap" x1="80" y1="7" x2="80" y2="45" transform="rotate(234 80 80)"/>
  <line class="gap" x1="80" y1="7" x2="80" y2="45" transform="rotate(324 80 80)"/>
  <line class="gap" x1="80" y1="7" x2="80" y2="45" transform="rotate(342 80 80)"/>
  <text x="128" y="104">65%</text><text x="28" y="71">25%</text><text x="55" y="32">5%</text><text x="72" y="27">5%</text>
</svg>
<div class="abs tilt-title" style="left:671px;top:933px">Dividend</div>
<ul class="abs tilt-list" style="left:671px;top:974px">
  <li><i class="blue"></i>Divident- Players</li>
  <li><i class="red"></i>Stocks</li>
  <li><i class="green"></i>Government Bonds</li>
  <li><i class="purple"></i>Corporate Bonds</li>
</ul>

<div class="abs rule rule-bottom"></div>
</body>
</html>
```